Simple Business Cards for Self-employed Coach

Simple business card with a design that includes the QLT logo.
Using either only the logo color or additional colors that match the logo.

Meridian Guides reach deeply into the past, gathering wisdom from East and West, while still staying current with the frontiers of new discovery in cognitive science, genetics, and other disciplines. see https://www.brightharborpath.example/what-is-integral-coaching/

Target Market(s)

Coaching Clients in Tokyo /Asia; in business organizations, but also outside

Industry/Entity Type

Life Coaching

Contact Information for Business Card

Lukas Brenning
Certified Meridian Guide

3-2-48 Kamiyoshi
Nakarino 164-0392
Tokyo, Japan

Phone: +81 70 4817 5062
E-Mail: lukas.brenning@mailora.example

Font styles to use
Sans Serif

Colors
00a990

Requirements
Must have
• include uploaded logo
• color fitting with QLT logo color
Nice to have
• simple, elegant design
Should not have
• clutter

```html
<!DOCTYPE html>
<html lang="en">
<head>
<meta charset="utf-8">
<title>Lukas Brenning – Business Card</title>
<link rel="stylesheet" href="https://fonts.googleapis.com/css2?family=Source+Sans+3:wght@400;600;700&display=swap">
<style>
  :root {
    --page-bg: #f7f7f7;
    --teal-light: #34b49c;
    --teal-dark: #1f9d86;
    --ink: #ffffff;
  }
  * { box-sizing: border-box; margin: 0; padding: 0; }
  html, body {
    width: 1200px;
    height: 1011px;
    overflow: hidden;
    background: var(--page-bg);
    font-family: "Source Sans 3", "Myriad Pro", Arial, sans-serif;
  }
  .business-card {
    position: absolute;
    left: 160px;
    top: 230px;
    width: 880px;
    height: 550px;
    background: linear-gradient(180deg, var(--teal-light) 0%, var(--teal-dark) 100%);
    color: var(--ink);
    box-shadow: 0 10px 30px rgba(0,0,0,0.08);
  }
  .brand {
    position: absolute;
    left: 80px;
    top: 150px;
    display: flex;
    align-items: center;
    gap: 16px;
  }
  .brand-square {
    width: 46px;
    height: 46px;
    border: 4px solid var(--ink);
  }
  .brand-name {
    font-size: 62px;
    font-weight: 700;
    letter-spacing: 10px;
    line-height: 1;
  }
  .contact-block {
    position: absolute;
    left: 470px;
    top: 150px;
    width: 360px;
  }
  .person-name {
    font-size: 42px;
    font-weight: 700;
    text-transform: uppercase;
    letter-spacing: -0.5px;
    line-height: 1.05;
  }
  .person-title {
    font-size: 20px;
    font-weight: 400;
    text-transform: uppercase;
    letter-spacing: -0.2px;
    margin-top: 6px;
  }
  .address {
    font-style: normal;
    text-align: center;
    font-size: 20px;
    line-height: 1.3;
    margin-top: 26px;
    padding-right: 40px;
  }
  .contact-lines {
    list-style: none;
    font-size: 20px;
    line-height: 1.3;
    margin-top: 20px;
    margin-left: -20px;
  }
  .contact-lines .label { font-weight: 700; }
</style>
</head>
<body>
  <section class="business-card">
    <div class="brand">
      <span class="brand-square"></span>
      <span class="brand-name">QLT</span>
    </div>
    <div class="contact-block">
      <h1 class="person-name">Lukas Brenning</h1>
      <p class="person-title">Certified Meridian Guide</p>
      <address class="address">
        3-2-48 Kamiyoshi<br>
        Nakarino 164-0392<br>
        Tokyo, Japan
      </address>
      <ul class="contact-lines">
        <li><span class="label">T:</span> +81 70 4817 5062</li>
        <li><span class="label">E:</span> lukas.brenning@mailora.example</li>
      </ul>
    </div>
  </section>
</body>
</html>
```